Record Sales in.. La Jolla | California

We need a CLEAN and MODERN looking flyer for a property. SIMPLE but CLEAN and cutting edge. We would like to use the logo attached at the bottom of the page. We prefer to only have the flyer front and back. If its necessary - we can do 2 pages.

--

Below is the Information/Stats we would like to include:

4318 Heron Court, La Jolla, CA | "The Cedar Loft"
- 4th Highest Sale in History of La Jolla's Highly Desirable Fern Hollow Community
- Recognized Internationally as a "One-of-a-Kind" Architectural Masterpiece
- Featured on Real Estate TV Show "Coastal Prestige Homes"

3814 Vereda Lumo, La Jolla, CA | Marisol Heights
- 2nd Highest Sale Price
- 3rd Highest Price Per S/F since 1997
- Extensive Pre-MLS Marketing. Sold on Day 1 of Listing

Client Testimonials:

4318 Heron Court
"Ned sold my oceanfront home in La Jolla and literally found the 'needle- in-the-hay-stack' cash buyer through his smart and targeted marketing backed by top notch Whitcombe Global Estates. He is an excellent communicator and negotiator and stays the course through thick and thin until a property is sold, while never losing focus on his #1 goal: to make his client happy. Definitely my agent of choice for any future transaction (buy or sell) and he should be yours too."

3814 Vereda Lumo
"We feel so lucky and fortunate to have found Ned. He promised me he would handle our sale from beginning to the end. Not only did Ned keep his promise, he went above & beyond to make sure the transaction stays at its course and time. Ned far exceeded our expectations in the price of the sale. I definitely will recommend Ned to all my family and friends. Thank you, Ned for an amazing experience."

--

Also include the Agents name and Contact Information below our logo:
- Ned Falworth | (858) 555-0172 | Ned@HOMQ-VT.example

Target Market(s)

Luxury Real Estate

Industry/Entity Type

Property

Colors

Designer to choose colors to be used in the design.

Requirements
Nice to have
• Unique & Modern Design

```html
<!DOCTYPE html>
<html lang="en">
<head>
<meta charset="utf-8">
<title>3814 Vereda Lumo — Marisol Heights</title>
<link rel="stylesheet" href="https://fonts.googleapis.com/css2?family=Montserrat:ital,wght@0,300;0,400;0,500;0,600;0,700;1,300&display=swap">
<style>
  :root {
    --navy: #1c2b57;
    --panel: #e4e5ea;
    --paper: #ffffff;
    --muted: #9a9ca3;
    --white: #ffffff;
  }
  * { margin: 0; padding: 0; box-sizing: border-box; }
  html, body { width: 887px; height: 1200px; overflow: hidden; background: var(--paper); }
  body { position: relative; font-family: "Montserrat", Arial, sans-serif; color: var(--navy); }

  .hero-photo {
    position: absolute; left: 67px; top: 67px; width: 753px; height: 561px;
    background:
      linear-gradient(90deg, rgba(0,0,0,0) 58%, rgba(92,156,210,0.55) 70%, rgba(120,180,220,0.35) 100%),
      linear-gradient(180deg, #ece8e0 0%, #b47a3f 28%, #a86a33 45%, #d9cfc3 70%, #e6ddd2 100%);
  }

  .feature-panel {
    position: absolute; left: 67px; top: 628px; width: 753px; height: 300px;
    background: var(--panel);
  }

  .title-banner { position: absolute; left: 67px; top: 579px; width: 551px; height: 121px; }
  .title-banner svg { position: absolute; inset: 0; }
  .title-banner .address {
    position: absolute; left: 50px; top: 16px;
    font-weight: 300; font-size: 25px; color: var(--white); letter-spacing: 0.3px;
  }
  .title-banner .estate-name {
    position: absolute; left: 48px; top: 55px;
    font-weight: 300; font-size: 43px; color: var(--white); letter-spacing: 2.5px; text-transform: uppercase;
  }

  .sale-facts { position: absolute; left: 115px; top: 760px; list-style: none; }
  .sale-facts li { font-weight: 500; font-size: 16px; line-height: 22px; margin-bottom: 14px; }

  .view-photo {
    position: absolute; left: 459px; top: 737px; width: 305px; height: 155px;
    background: linear-gradient(180deg, #7fb6e3 0%, #2e6fb0 18%, #6f8f5a 45%, #4b6a3c 70%, #c9c3b8 100%);
  }

  .testimonials { position: absolute; left: 115px; top: 957px; width: 275px; }
  .testimonials .label {
    display: inline-block; border: 1px solid var(--navy);
    font-size: 12px; font-weight: 500; padding: 2px 4px 1px;
  }
  .testimonials .property { margin-top: 10px; font-size: 9px; color: var(--muted); font-weight: 400; }
  .testimonials blockquote {
    font-size: 9.1px; line-height: 14.6px; font-style: italic; font-weight: 300; color: var(--muted);
  }

  .brokerage { position: absolute; left: 420px; top: 966px; width: 360px; text-align: center; }
  .brokerage .team { font-size: 27px; font-weight: 400; letter-spacing: 0.5px; }
  .brokerage .firm { margin-top: 6px; font-size: 15px; font-weight: 400; letter-spacing: 0.5px; }
  .brokerage .firm::before {
    content: ""; display: inline-block; width: 8px; height: 8px; background: var(--navy);
    margin-right: 8px; vertical-align: 2px;
  }

  .agent-contact {
    position: absolute; left: 443px; top: 1068px; font-size: 15.5px; font-weight: 400;
  }
  .agent-contact strong { font-weight: 700; }

  .footer-rule { position: absolute; left: 67px; top: 1124px; width: 753px; height: 9px; }
</style>
</head>
<body>
  <div class="hero-photo" role="img" aria-label="Photo of a bright kitchen with wood cabinets, a granite island and a glass dining table opening onto an ocean-view deck"></div>

  <div class="feature-panel"></div>

  <div class="title-banner">
    <svg width="551" height="121" viewBox="0 0 551 121" aria-hidden="true">
      <polygon points="0,0 530,0 551,121 0,121" fill="#1c2b57"/>
    </svg>
    <div class="address">3814 Vereda Lumo, La Jolla, CA</div>
    <div class="estate-name">Marisol Heights</div>
  </div>

  <ul class="sale-facts">
    <li>2nd Highest Sale Price</li>
    <li>3rd Highest Price Per S/F since 1997</li>
    <li>Extensive Pre-MLS Marketing.<br>Sold on Day 1 of Listing</li>
  </ul>

  <div class="view-photo" role="img" aria-label="Photo of a deck lounge with cushioned seating overlooking the coastline and ocean"></div>

  <section class="testimonials">
    <span class="label">Client Testimonials</span>
    <p class="property">3814 Vereda Lumo</p>
    <blockquote>“We feel so lucky and fortunate to have found Ned. He promised me he would handle our sale from beginning to the end. Not only did Ned keep his promise, he went above &amp; beyond to make sure the transaction stays at its course and time. Ned far exceeded our expectations in the price of the sale. I definitely will recommend Ned to all my family and friends. Thank you, Ned for an amazing experience.”</blockquote>
  </section>

  <div class="brokerage">
    <div class="team">Shoreline Crest Group</div>
    <div class="firm">Westbay | Whitcombe Global Estates</div>
  </div>

  <p class="agent-contact"><strong>Ned Falworth</strong> (858) 555-0172 | Ned@HOMQ-VT.example</p>

  <svg class="footer-rule" width="753" height="9" viewBox="0 0 753 9" aria-hidden="true">
    <polygon points="0,0 547,0 543,9 0,9" fill="#1c2b57"/>
    <polygon points="553,0 753,0 753,9 549,9" fill="#1c2b57"/>
  </svg>
</body>
</html>
```